Logo und Visitenkarte/Briefpapier für Taxiunternehmen
Zielgruppe
Taxiunternehmen / Dienstleistungen
Aufgabenstellung
Erstellen eines einprägsamen Logos
Schlagworte: Vertrauen, Wohlfühlen, Sicherheit
Das neue Briefpapier muss von uns veränderbar sein, da wir noch nicht alle Daten haben wie Steuernummer und USt-ID, bitte aber schon als Dummy anlegen.
Beispiele die mir gefallen:
#1: http://www.lorvenbask.com/images/brisk-lines/brisk-lines-logo-samples.jpg
#2: http://www.quendora.com/blog/wp-content/uploads/2013/04/logo_blog.png
Viel Spaß und Danke im Voraus

```html
<!DOCTYPE html>
<html lang="de">
<head>
<meta charset="utf-8">
<title>Taxi Veloran – Briefpapier und Visitenkarten</title>
<link rel="stylesheet" href="https://fonts.googleapis.com/css2?family=Alegreya+Sans:wght@500;700&display=swap">
<style>
  :root{
    --page:#ffffff;
    --paper:#e5e4e0;
    --card:#fbe96c;
    --card-light:#fdf6c4;
    --amber:#f6bd16;
    --ink:#2e2c2a;
    --box-line:#333333;
    --faint:#efecd6;
  }
  *{box-sizing:border-box;margin:0;padding:0}
  html,body{width:763px;height:1200px;overflow:hidden;background:var(--page)}
  body{position:relative;font-family:"Alegreya Sans",sans-serif;color:var(--ink);font-weight:500}

  .letterhead{position:absolute;left:167px;top:61px;width:453px;height:641px;background:var(--paper)}
  .brand{position:absolute;display:flex;align-items:center;gap:10px}
  .brand-square{background:var(--amber);border:2px solid var(--box-line);border-radius:5px}
  .brand-name{font-weight:700;color:var(--ink);line-height:1}
  .letterhead .brand{left:27px;top:58px}
  .letterhead .brand-square{width:38px;height:38px}
  .letterhead .brand-name{font-size:46px}

  .letterhead .company{position:absolute;left:265px;top:36px;font-size:26px;font-weight:700}
  .letterhead .address{position:absolute;left:265px;top:83px;font-size:15px;line-height:28px}
  .letterhead .watermark{position:absolute;left:0;right:0;top:230px;text-align:center;font-size:120px;font-weight:700;color:var(--faint);line-height:1}
  .letterhead .contact{position:absolute;left:20px;top:548px;font-size:15px;line-height:28px}

  .corner-band{position:absolute;border-radius:4px;background:linear-gradient(90deg,#ffffff,var(--amber))}
  .letterhead .corner-band{left:255px;top:609px;width:182px;height:21px}
  .card .corner-band{left:157px;top:115px;width:76px;height:9px;border-radius:2px}

  .card{position:absolute;width:239px;height:132px;background:var(--card);border-radius:0 10px 0 10px}
  .card-front-a{left:130px;top:792px}
  .card-front-b{left:130px;top:1010px;background:linear-gradient(150deg,var(--card) 45%,var(--card-light) 75%,#ffffff 95%)}
  .card-back{left:395px;top:893px;border-radius:0 0 10px 10px}

  .card .lines{position:absolute;font-size:11.5px;line-height:21px}
  .card .lines .name{font-size:12.5px}
  .card .brand{gap:6px}
  .card .brand-square{width:16px;height:16px;border-width:1.5px;border-radius:3px}
  .card .brand-name{font-size:22px}
  .card .id{position:absolute;font-size:8px;transform:rotate(-90deg);transform-origin:left top;white-space:nowrap}

  .card-back .brand{left:50%;top:50%;transform:translate(-50%,-50%)}
  .card-back .brand-square{width:26px;height:26px;border-radius:4px}
  .card-back .brand-name{font-size:38px}
</style>
</head>
<body>

<section class="letterhead" aria-label="Briefpapier">
  <div class="brand"><span class="brand-square"></span><span class="brand-name">Veloran</span></div>
  <h1 class="company">Taxi Veloran</h1>
  <p class="address">Lindenhofweg 48a<br>22761 Hamburg</p>
  <div class="watermark" aria-hidden="true">Veloran</div>
  <p class="contact">Tel: 040/57 92 63<br>Mobil: 0176/48 26 13 90<br>Rufnetz ID: 4821KT</p>
  <div class="corner-band" role="img" aria-label="Dekoratives Eckmotiv in Bernstein und Weiß"></div>
</section>

<section class="card card-front-a" aria-label="Visitenkarte Vorderseite">
  <p class="lines" style="left:9px;top:4px"><span class="name">Taxi Veloran</span><br>Lindenhofweg 48a<br>22761 Hamburg</p>
  <div class="brand" style="left:116px;top:36px"><span class="brand-square"></span><span class="brand-name">Veloran</span></div>
  <p class="lines" style="left:9px;top:84px">Tel.: 040 / 57 92 63<br>Mobil: 0176 / 48 26 13 90</p>
  <span class="id" style="left:222px;top:86px">Rufnetz ID: 4821KT</span>
  <div class="corner-band" role="img" aria-label="Dekoratives Eckmotiv in Bernstein und Weiß"></div>
</section>

<section class="card card-back" aria-label="Visitenkarte Rückseite">
  <div class="brand"><span class="brand-square"></span><span class="brand-name">Veloran</span></div>
</section>

<section class="card card-front-b" aria-label="Visitenkarte Variante">
  <div class="brand" style="left:9px;top:22px"><span class="brand-square"></span><span class="brand-name">Veloran</span></div>
  <p class="lines" style="left:120px;top:7px"><span class="name">Taxi Veloran</span><br>Lindenhofweg 48a<br>22761 Hamburg</p>
  <p class="lines" style="left:9px;top:82px">Tel.: 040 / 57 92 63<br>Mobil: 0176 / 48 26 13 90</p>
  <span class="id" style="left:222px;top:86px">Rufnetz ID: 4821KT</span>
  <div class="corner-band" role="img" aria-label="Dekoratives Eckmotiv in Bernstein und Weiß"></div>
</section>

</body>
</html>
```